TITLE: What Makes My Child’s Playing Talent Grow? SUB-TITLE: A Mother’s Plain Talk Manual for Coaching...

My book is for parents who have young children that are really into sports. My book empowers parents so they can motivate their children to succeed. It deals with sports psychology. Both my title and subtitle should be easy to read. Ideally, I would like a picture of young athlete(s) on the title. I have uploaded files of some books on Brindlemart that deal with the same subject. The last two files are 1) my company logo, please try to include these colors 2) an ebook cover I put together myself. You will notice an On-line bonus in the middle of the book, this Bonus needs to be on the cover.

Target Market(s)

Parents with children who play sports at a high level

Colors

Designer to choose colors to be used in the design.

Requirements
Must have
• Online Bonus feature as per my example.
• Dimensions: Pagelux = The ideal size of your eBook cover art is a height/width ratio of 1.6:1. This means that for every 1,000 pixels in width, the image should be 1,600 pixels in height.
Nice to have
• picture of a young athlete or young athletes

```html
<!DOCTYPE html>
<html lang="en">
<head>
<meta charset="utf-8">
<title>What Makes My Child’s Playing Talent Grow?</title>
<link rel="stylesheet" href="https://fonts.googleapis.com/css2?family=Oswald:wght@400;500;600&display=swap">
<style>
  :root {
    --paper: #f4f4f3;
    --orange: #f39a2b;
    --brown: #574740;
    --white: #ffffff;
    --road-dark: #6e6878;
    --road-light: #b9b4bd;
    --line-gold: #e0aa48;
  }
  * { margin: 0; padding: 0; box-sizing: border-box; }
  html, body { width: 750px; height: 1200px; overflow: hidden; background: var(--paper); }
  .cover {
    position: relative;
    width: 750px;
    height: 1200px;
    background: var(--paper);
    font-family: "Oswald", sans-serif;
    color: var(--brown);
    overflow: hidden;
  }
  .hero-photo {
    position: absolute;
    left: 0; top: 0;
    width: 750px; height: 660px;
    background:
      radial-gradient(ellipse 260px 260px at 390px 230px, #3b7fc8 0%, #5a8fc6 35%, rgba(244,244,243,0) 75%),
      linear-gradient(180deg, var(--paper) 0%, #e4e2e6 30%, var(--road-light) 55%, var(--road-dark) 88%);
  }
  .start-line {
    position: absolute;
    left: 0; top: 606px;
    width: 750px; height: 54px;
    background: var(--line-gold);
  }
  .brand {
    position: absolute;
    left: 58px; top: 62px;
    display: flex; align-items: center; gap: 12px;
  }
  .brand-dot {
    width: 40px; height: 40px; border-radius: 50%;
    background: var(--orange);
  }
  .brand-name {
    font-weight: 500; font-size: 22px; letter-spacing: 1px;
    color: var(--brown); text-transform: uppercase;
  }
  .author {
    position: absolute;
    right: 56px; top: 58px;
    font-weight: 500; font-size: 25px; letter-spacing: 2.5px;
    color: var(--brown);
  }
  .bonus {
    position: absolute;
    left: 255px; top: 467px;
    width: 240px; height: 240px;
    border-radius: 50%;
    background: var(--orange);
    text-align: center;
    color: var(--brown);
    text-transform: uppercase;
    padding-top: 40px;
  }
  .bonus-line { display: block; font-weight: 400; font-size: 24px; line-height: 1.1; letter-spacing: 1px; }
  .bonus-value { display: block; margin-top: 8px; font-weight: 600; font-size: 36px; line-height: 1.1; color: var(--white); }
  .bonus-note { display: block; margin-top: 4px; font-size: 13px; text-transform: none; }
  .title-line {
    position: absolute;
    left: 0; width: 750px;
    text-align: center;
    text-transform: uppercase;
    font-weight: 500;
    line-height: 1;
    white-space: nowrap;
  }
  .title-lead { top: 720px; font-size: 100px; color: var(--orange); }
  .title-mid  { top: 811px; font-size: 72px; color: var(--brown); }
  .title-end  { top: 866px; font-size: 160px; color: var(--brown); }
  .subtitle-line {
    position: absolute;
    left: 0; width: 750px;
    text-align: center; text-transform: uppercase;
    line-height: 1; white-space: nowrap;
    color: var(--brown);
  }
  .subtitle-lead { top: 1072px; font-weight: 400; font-size: 20px; letter-spacing: 2.4px; }
  .subtitle-end  { top: 1109px; font-weight: 500; font-size: 32px; letter-spacing: 2px; }
</style>
</head>
<body>
<main class="cover">
  <div class="hero-photo" role="img" aria-label="Photo of a young boy in a blue sports kit crouched in a sprint start position on an asphalt track"></div>
  <div class="start-line"></div>

  <div class="brand">
    <span class="brand-dot"></span>
    <span class="brand-name">Mindpace Coaching</span>
  </div>
  <div class="author">LEON VARGAS</div>

  <div class="bonus">
    <span class="bonus-line">Free</span>
    <span class="bonus-line">Online</span>
    <span class="bonus-line">Workshop</span>
    <span class="bonus-value">$170 VALUE</span>
    <span class="bonus-note">details inside</span>
  </div>

  <h1>
    <span class="title-line title-lead">What Makes My</span>
    <span class="title-line title-mid">Child’s Playing Talent</span>
    <span class="title-line title-end">Grow?</span>
  </h1>

  <p>
    <span class="subtitle-line subtitle-lead">A Mother’s Plain Talk Manual for Coaching</span>
    <span class="subtitle-line subtitle-end">Confident, Focused and Resilent Athletes</span>
  </p>
</main>
</body>
</html>
```